Beauty Studio Business Card Design

its a new business & I want something different and classy
the strips are part of my decor

Target Market(s)

young girls and mature women

Industry/Entity Type

Business

Contact Information for Business Card

Frae-la-mu 26 0459817362 ABN # all on the front
address on the back + apt times & maybe my name
I would like black & white strips & fancy font with a fancy border around Frae-la-mu

```html
<!DOCTYPE html>
<html lang="en">
<head>
<meta charset="utf-8">
<title>Frae-la-mu Business Card</title>
<link rel="stylesheet" href="https://fonts.googleapis.com/css2?family=Quicksand:wght@300;400&family=Montserrat:wght@500&family=Great+Vibes&display=swap">
<style>
  :root {
    --page: #ffffff;
    --card: #0c0c0c;
    --card-glow: #2e2e2e;
    --gold: #f0a21e;
    --white: #f4f4f4;
    --soft-grey: #c8c8c8;
    --faint: rgba(255, 255, 255, 0.08);
    --ornament-light: rgba(235, 235, 235, 0.42);
    --ornament-fade: rgba(235, 235, 235, 0);
    --stripe-dark: #1c1c1c;
    --stripe-mid: #7c7c7c;
    --stripe-light: #b4b4b4;
  }
  * { margin: 0; padding: 0; box-sizing: border-box; }
  html, body {
    width: 1200px;
    height: 444px;
    overflow: hidden;
    background: var(--page);
  }
  .canvas {
    position: relative;
    width: 1200px;
    height: 444px;
  }
  .card {
    position: absolute;
    top: 15px;
    width: 556px;
    height: 343px;
    overflow: hidden;
    background: var(--card);
  }
  .card--front {
    left: 24px;
    background: radial-gradient(ellipse 55% 45% at 40% 100%, var(--card-glow) 0%, var(--card) 70%);
  }
  .card--back {
    left: 624px;
    background: radial-gradient(ellipse 65% 55% at 72% 50%, #262626 0%, var(--card) 75%);
  }
  .ornament {
    position: absolute;
    border-radius: 6px;
  }
  .ornament--lower-left {
    background: linear-gradient(45deg, var(--ornament-light) 0%, var(--ornament-light) 30%, var(--ornament-fade) 75%);
  }
  .ornament--upper-right {
    background: linear-gradient(225deg, var(--ornament-light) 0%, var(--ornament-light) 30%, var(--ornament-fade) 75%);
  }
  .ornament--faint { opacity: 0.18; }
  .brand-name {
    position: absolute;
    font-family: "Quicksand", sans-serif;
    font-weight: 400;
    color: var(--gold);
    white-space: nowrap;
  }
  .card--front .brand-name {
    left: 150px;
    top: 146px;
    font-size: 50px;
  }
  .card--back .brand-name {
    left: 92px;
    top: 80px;
    font-size: 21px;
  }
  .business-number {
    position: absolute;
    left: 184px;
    top: 290px;
    font-family: "Quicksand", sans-serif;
    font-weight: 300;
    font-size: 17px;
    letter-spacing: 2px;
    word-spacing: 8px;
    color: var(--soft-grey);
  }
  .brand-watermark {
    position: absolute;
    left: 110px;
    top: 178px;
    font-family: "Quicksand", sans-serif;
    font-weight: 400;
    font-size: 80px;
    color: var(--faint);
    white-space: nowrap;
  }
  .stylist-name {
    position: absolute;
    left: 109px;
    top: 164px;
    font-family: "Montserrat", sans-serif;
    font-weight: 500;
    font-size: 22px;
    letter-spacing: 2.5px;
    color: var(--white);
  }
  .stylist-role {
    position: absolute;
    left: 108px;
    top: 198px;
    font-family: "Great Vibes", cursive;
    font-size: 24px;
    color: var(--white);
  }
  .phone {
    position: absolute;
    right: 26px;
    top: 223px;
    font-family: "Quicksand", sans-serif;
    font-weight: 400;
    font-size: 17px;
    letter-spacing: 0.6px;
    color: var(--white);
  }
  .stripe-band {
    position: absolute;
    left: 0;
    bottom: 0;
    width: 556px;
    height: 86px;
    background:
      linear-gradient(180deg, rgba(255,255,255,0.18) 0%, rgba(0,0,0,0) 40%, rgba(0,0,0,0.25) 100%),
      linear-gradient(90deg, var(--stripe-mid) 0%, var(--stripe-light) 25%, var(--stripe-mid) 50%, var(--stripe-light) 75%, var(--stripe-mid) 100%);
  }
</style>
</head>
<body>
<main class="canvas">
  <section class="card card--front" aria-label="Card front">
    <div class="ornament ornament--lower-left" role="img" aria-label="White floral scroll corner ornament" style="left:73px; top:128px; width:108px; height:110px;"></div>
    <div class="ornament ornament--upper-right" role="img" aria-label="White floral scroll corner ornament" style="left:359px; top:82px; width:108px; height:110px;"></div>
    <div class="brand-name">Frae-la-mu</div>
    <div class="business-number">26 0459817362 ABN</div>
  </section>

  <section class="card card--back" aria-label="Card back">
    <div class="ornament ornament--upper-right ornament--faint" role="img" aria-label="Faint floral scroll decoration" style="left:410px; top:120px; width:140px; height:80px;"></div>
    <div class="ornament ornament--lower-left ornament--faint" role="img" aria-label="Faint floral scroll decoration" style="left:16px; top:180px; width:64px; height:70px;"></div>
    <div class="brand-watermark" aria-hidden="true">Frae-la-mu</div>
    <div class="ornament ornament--lower-left" role="img" aria-label="White floral scroll corner ornament" style="left:59px; top:77px; width:52px; height:48px;"></div>
    <div class="ornament ornament--upper-right" role="img" aria-label="White floral scroll corner ornament" style="left:196px; top:57px; width:48px; height:52px;"></div>
    <div class="brand-name">Frae-la-mu</div>
    <div class="stylist-name">JANE DOE</div>
    <div class="stylist-role">Stylist</div>
    <div class="phone">Phone: 123 456789</div>
    <div class="stripe-band" role="img" aria-label="Black and white zebra stripe pattern band"></div>
  </section>
</main>
</body>
</html>
```